Letterhead to Introduce a 'Sister' Company.

What I am needing is a design for a letter head to introduce our current customers base of (KT Alarm) customers to our new service, 'Kestrel Tide Solar Brokers'

```html
<!DOCTYPE html>
<html lang="en">
<head>
<meta charset="utf-8">
<title>Kestrel Tide Solar Brokers – Letterhead</title>
<link href="https://fonts.googleapis.com/css2?family=Montserrat:wght@400;600&display=swap" rel="stylesheet">
<style>
  :root {
    --brand-blue: #124a82;
    --band-blue: #0a57a0;
    --sun-orange: #f29a1f;
    --sun-tint: #fdf5ea;
    --accent-green: #4cb848;
    --ink: #222222;
    --paper: #ffffff;
  }
  html, body {
    margin: 0;
    padding: 0;
    width: 900px;
    height: 1200px;
    overflow: hidden;
    background: var(--paper);
  }
  .letterhead {
    position: relative;
    width: 900px;
    height: 1200px;
    background: var(--paper);
    overflow: hidden;
    font-family: "Montserrat", sans-serif;
    color: var(--ink);
  }

  /* Header */
  .brand-mark {
    position: absolute;
    left: 420px;
    top: 40px;
    width: 60px;
    height: 60px;
    border-radius: 50%;
    background: var(--sun-orange);
  }
  .brand-name {
    position: absolute;
    left: 0;
    width: 900px;
    top: 118px;
    text-align: center;
    color: var(--brand-blue);
    font-weight: 600;
    line-height: 1;
  }
  .brand-name .primary {
    display: block;
    font-size: 29px;
    letter-spacing: 0.5px;
  }
  .brand-name .secondary {
    display: block;
    margin-top: 10px;
    font-size: 14px;
    letter-spacing: 2.5px;
  }
  .header-rule {
    position: absolute;
    top: 166px;
    height: 1.5px;
    background: var(--brand-blue);
  }
  .header-rule.left { left: 0; width: 310px; }
  .header-rule.right { left: 590px; width: 310px; }

  /* Decorative sun area */
  .sun-decoration {
    position: absolute;
    left: 290px;
    top: 585px;
    width: 720px;
    height: 720px;
    background: radial-gradient(circle at 50% 50%, var(--sun-tint) 0%, var(--sun-tint) 48%, rgba(253,245,234,0.55) 62%, rgba(253,245,234,0) 72%);
  }

  /* Footer */
  .contact-list {
    position: absolute;
    right: 482px;
    top: 1115px;
    margin: 0;
    padding: 0;
    list-style: none;
    text-align: right;
    font-size: 13px;
    letter-spacing: 0.4px;
  }
  .contact-list li {
    display: flex;
    align-items: center;
    justify-content: flex-end;
    height: 17px;
  }
  .contact-list svg {
    width: 9px;
    height: 9px;
    margin-left: 9px;
    fill: var(--accent-green);
  }
  .footer-divider {
    position: absolute;
    left: 433px;
    top: 1118px;
    width: 1.5px;
    height: 46px;
    background: var(--ink);
  }
  .company-name {
    position: absolute;
    left: 460px;
    top: 1117px;
    font-size: 27px;
    font-weight: 600;
    color: var(--brand-blue);
    line-height: 1;
    letter-spacing: 0.5px;
  }
  .company-address {
    position: absolute;
    left: 461px;
    top: 1150px;
    font-size: 12.5px;
    letter-spacing: 0.6px;
  }
  .footer-band {
    position: absolute;
    left: 0;
    bottom: 0;
    width: 900px;
    height: 12px;
    background: var(--band-blue);
  }
</style>
</head>
<body>
  <div class="letterhead">
    <header>
      <div class="brand-mark"></div>
      <div class="brand-name">
        <span class="primary">KESTREL TIDE</span>
        <span class="secondary">SOLAR BROKERS</span>
      </div>
      <div class="header-rule left"></div>
      <div class="header-rule right"></div>
    </header>

    <div class="sun-decoration" role="img" aria-label="Large faint sunburst decoration in pale cream"></div>

    <footer>
      <ul class="contact-list">
        <li>555-014-2290
          <svg viewBox="0 0 10 10" aria-hidden="true"><path d="M2 0.5 L3.6 2.6 L2.7 3.6 C3.3 5 4.8 6.6 6.3 7.2 L7.3 6.3 L9.5 7.9 L8.4 9.5 C4.5 9.5 0.5 5.5 0.5 1.5 Z"/></svg>
        </li>
        <li>info@kthomesecurity.com
          <svg viewBox="0 0 10 10" aria-hidden="true"><path d="M0 2 H10 V8.5 H0 Z M0.6 2.4 L5 5.6 L9.4 2.4" stroke="#fff" stroke-width="0.8"/></svg>
        </li>
        <li>www.kthomesecurity.com
          <svg viewBox="0 0 10 10" aria-hidden="true"><circle cx="5" cy="5" r="4.8"/><path d="M0.5 5 H9.5 M5 0.3 V9.7 M5 0.4 C2.6 3 2.6 7 5 9.6 M5 0.4 C7.4 3 7.4 7 5 9.6" stroke="#fff" stroke-width="0.6" fill="none"/></svg>
        </li>
      </ul>
      <div class="footer-divider"></div>
      <div class="company-name">KT Alarm</div>
      <div class="company-address">PO Box 2207. Harborview, WA 98000</div>
      <div class="footer-band"></div>
    </footer>
  </div>
</body>
</html>
```